Celebrating 50 Years of Brannock

This will be a vinyl 10 foot by 8 foot large banner hung at a 50 year celebration. Attached you will find the word document that it will need to have on it and the logo and the invitation - both in all different formats - be creative as possible while staying with brand. We want a dynamic representation of the accomplishments over the last 50 years.

Target Market(s)

To use at a function to celebrate our 50th years in business

Industry/Entity Type

Hospitality

Colors

Designer to choose colors to be used in the design.

Requirements
Must have
• the attached logo and the events
Nice to have
• branding to tie into
Should not have
• should not boring and appear flat

```html
<!DOCTYPE html>
<html lang="en">
<head>
<meta charset="utf-8">
<title>Brannock Family 50th Anniversary Luncheon Banner</title>
<link rel="stylesheet" href="https://fonts.googleapis.com/css2?family=Cinzel:wght@600;700&family=Lora:wght@400;500;700&family=Cormorant+Garamond:ital,wght@1,600;1,700&display=swap">
<style>
  :root {
    --page: #eef1f5;
    --grey-light: #f4f4f4;
    --grey-mid: #c9c9c9;
    --blue: #1f86d1;
    --blue-deep: #1677c0;
    --white: #ffffff;
    --ink: #2b2b2b;
    --ink-soft: #555555;
    --navy: #1b4d8c;
  }
  html, body {
    margin: 0;
    width: 1200px;
    height: 1200px;
    overflow: hidden;
    background: var(--page);
  }
  .banner {
    position: absolute;
    left: 50px;
    top: 270px;
    width: 1100px;
    height: 660px;
    background: var(--white);
    box-shadow: 0 12px 30px rgba(0,0,0,0.18);
    overflow: hidden;
  }
  .banner__header {
    position: absolute;
    left: 0; top: 0;
    width: 100%; height: 150px;
    background: linear-gradient(90deg, var(--grey-mid) 0%, var(--grey-light) 45%, var(--grey-light) 70%, var(--grey-mid) 100%);
  }
  .banner__body {
    position: absolute;
    left: 0; top: 150px;
    width: 100%; height: 390px;
    background: linear-gradient(180deg, var(--blue) 0%, var(--blue-deep) 100%);
  }
  .banner__footer {
    position: absolute;
    left: 0; top: 540px;
    width: 100%; height: 120px;
    background: var(--white);
  }
  .brand-seal {
    position: absolute;
    left: 60px; top: 20px;
    width: 230px; height: 180px;
    border-radius: 50%;
    background: var(--white);
    display: flex;
    align-items: center;
    justify-content: center;
    text-align: center;
    font-family: "Cinzel", serif;
    font-weight: 700;
    font-size: 24px;
    line-height: 1.25;
    color: var(--navy);
    letter-spacing: 1px;
  }
  .invite {
    position: absolute;
    left: 360px; top: 22px;
    width: 700px;
    text-align: center;
    color: var(--ink);
  }
  .invite__host {
    font-family: "Cinzel", serif;
    font-weight: 700;
    font-size: 31px;
    letter-spacing: 1px;
    margin: 0 0 4px;
  }
  .invite__line {
    font-family: "Lora", serif;
    font-size: 31px;
    letter-spacing: 2px;
    color: var(--ink-soft);
    margin: 0;
    line-height: 1.2;
  }
  .detail {
    position: absolute;
    border: 1.5px solid rgba(255,255,255,0.75);
    border-radius: 6px;
    color: var(--white);
    text-align: center;
    box-sizing: border-box;
  }
  .detail__label {
    position: absolute;
    top: -16px;
    left: 50%;
    transform: translateX(-50%);
    background: var(--blue);
    padding: 0 14px;
    font-family: "Cinzel", serif;
    font-weight: 700;
    font-size: 24px;
    letter-spacing: 1px;
    white-space: nowrap;
  }
  .detail__value {
    font-family: "Lora", serif;
    font-weight: 500;
    font-size: 23px;
    line-height: 1.35;
    margin: 0;
  }
  .detail__value strong { font-weight: 700; }
  .detail--date { left: 50px; top: 85px; width: 290px; height: 95px; padding-top: 20px; }
  .detail--time { left: 370px; top: 60px; width: 270px; height: 85px; padding-top: 26px; }
  .detail--where { left: 50px; top: 220px; width: 590px; height: 105px; padding-top: 24px; }
  .milestone {
    position: absolute;
    left: 700px; top: 25px;
    width: 360px;
    color: var(--white);
    font-family: "Cormorant Garamond", serif;
    font-style: italic;
  }
  .milestone__number {
    display: block;
    font-family: "Cinzel", serif;
    font-style: normal;
    font-weight: 700;
    font-size: 150px;
    line-height: 1;
    text-align: right;
    padding-right: 30px;
  }
  .milestone__years {
    display: block;
    font-weight: 700;
    font-size: 100px;
    line-height: 0.9;
    padding-left: 10px;
  }
  .milestone__tail {
    display: block;
    font-weight: 600;
    font-size: 38px;
    text-align: right;
    letter-spacing: 1px;
  }
  .contact {
    position: absolute;
    left: 90px; top: 28px;
    display: flex;
    align-items: center;
    gap: 24px;
  }
  .contact__phone {
    font-family: "Cinzel", serif;
    font-weight: 700;
    font-size: 54px;
    color: var(--ink);
    letter-spacing: 2px;
  }
</style>
</head>
<body>
  <main class="banner">
    <div class="banner__header"></div>
    <div class="banner__body">
      <div class="detail detail--date">
        <span class="detail__label">DATE</span>
        <p class="detail__value">Tuesday, May 15<br><strong>2018</strong></p>
      </div>
      <div class="detail detail--time">
        <span class="detail__label">TIME</span>
        <p class="detail__value"><strong>11 am - 1 pm</strong></p>
      </div>
      <div class="detail detail--where">
        <span class="detail__label">WHERE</span>
        <p class="detail__value">Stone Hollow Center 4190 Harlan Drive<br>Cedar Bend TN 37860</p>
      </div>
      <div class="milestone">
        <span class="milestone__number">50</span>
        <span class="milestone__years">years</span>
        <span class="milestone__tail">of business!</span>
      </div>
    </div>
    <div class="banner__footer">
      <div class="contact">
        <svg width="64" height="64" viewBox="0 0 64 64" aria-hidden="true">
          <circle cx="32" cy="32" r="29" fill="none" stroke="#1b2a3a" stroke-width="4"/>
          <path d="M22 18c2-1 4 0 5 2l2 5c1 2 0 3-1 4l-2 1c1 4 5 8 9 9l1-2c1-1 2-2 4-1l5 2c2 1 3 3 2 5l-1 2c-2 3-6 4-10 2-8-4-14-10-17-18-1-4 0-8 3-10z" fill="var(--blue)"/>
        </svg>
        <span class="contact__phone">865-555-0142</span>
      </div>
    </div>
    <div class="brand-seal">Brannock<br>Hospitality</div>
    <div class="invite">
      <p class="invite__host">BRANNOCK FAMILY CORDIALLY</p>
      <p class="invite__line">Invites you to</p>
      <p class="invite__line">a Luncheon to Celebrate</p>
    </div>
  </main>
</body>
</html>
```